Real Estate Flyer

I would like an A4 size flyer which has the same info 3 times and can be cut into three.
It will be used for letterbox drops for new listings (SELLING) and sold listings (SOLD). The flyer needs a heading (as above) and a space for a photo which is able to be changed for each new property. Needs to be blue, red and white. It also requires my photo, KLV logo, Marisska Thornbury logo and the following text:
"Are you considering selling? Call Marisska today for a complimentary market appraisal".
(KLV logo, Marisska Thornbury Sales Consultant logo and my photo can be found in uploaded files)

```html
<!DOCTYPE html>
<html lang="en">
<head>
<meta charset="utf-8">
<title>KLV Realty – Marisska Thornbury appraisal flyer</title>
<link rel="stylesheet" href="https://fonts.googleapis.com/css2?family=Open+Sans:wght@400;600&family=Tinos:wght@700&display=swap">
<style>
  :root {
    --red: #d62b2b;
    --red-deep: #c41f22;
    --navy: #0f2c5c;
    --navy-deep: #0b2450;
    --paper: #ececec;
    --white: #ffffff;
    --ink-grey: #6f6f6f;
    --photo-warm-a: #b89a74;
    --photo-warm-b: #3b3330;
  }
  * { box-sizing: border-box; margin: 0; padding: 0; }
  html, body { width: 1200px; height: 848px; overflow: hidden; background: var(--white); }
  .flyer { position: relative; width: 1200px; height: 848px; font-family: "Open Sans", Arial, sans-serif; }

  .strip { position: absolute; left: 0; width: 1200px; overflow: hidden; }
  .strip--red   { top: 0;   height: 283px; background: var(--red); }
  .strip--navy  { top: 283px; height: 282px; background: var(--navy); }
  .strip--white { top: 565px; height: 283px; background: var(--paper); }

  .agent-photo {
    position: absolute; left: 50px; top: 62px; width: 247px; height: 165px;
    background: linear-gradient(110deg, var(--photo-warm-a) 0%, #8f7a62 35%, var(--photo-warm-b) 70%, #6b5a4c 100%);
    box-shadow: 0 2px 6px rgba(0,0,0,0.35);
  }
  .strip--navy .agent-photo { top: 60px; left: 52px; }
  .strip--white .agent-photo { top: 60px; left: 58px; width: 240px; }

  .pitch { position: absolute; left: 0; top: 0; width: 900px; height: 100%; }
  .pitch__line { position: absolute; white-space: nowrap; }
  .pitch__ask  { left: 344px; top: 64px; font-size: 38px; }
  .pitch__call { left: 346px; top: 112px; font-size: 31px; }
  .pitch__offer{ left: 337px; top: 184px; font-size: 33px; }
  .pitch__name {
    font-family: "Tinos", "Times New Roman", serif; font-weight: 700;
    font-size: 58px; margin: 0 14px 0 12px; vertical-align: -6px;
  }

  .strip--red .pitch__line,
  .strip--navy .pitch__line { color: var(--white); }
  .strip--white .pitch__line { color: var(--red); }
  .strip--red .pitch__name,
  .strip--white .pitch__name { color: var(--navy); }
  .strip--navy .pitch__name { color: var(--red); }

  .brand-bar {
    position: absolute; left: 925px; top: 48px; width: 247px; height: 42px;
    background: var(--navy-deep); border: 2px solid #d8d8d8;
    color: var(--white); font-weight: 600; font-size: 22px;
    display: flex; align-items: center; justify-content: center; letter-spacing: 0.5px;
  }

  .agent-card {
    position: absolute; left: 908px; top: 102px; width: 275px; height: 133px;
    background: var(--white);
    display: flex; flex-direction: column; justify-content: center; padding-left: 72px;
  }
  .agent-card__mark {
    position: absolute; left: 26px; top: 48px; width: 34px; height: 34px; background: var(--red-deep);
  }
  .agent-card__name { font-size: 16px; color: #333333; letter-spacing: 0.6px; white-space: nowrap; }
  .agent-card__role { font-size: 11px; color: var(--ink-grey); letter-spacing: 1px; padding-left: 48px; }
  .agent-card__phone { font-size: 12px; color: var(--red-deep); padding-left: 58px; margin-top: 2px; }

  .strip--navy .brand-bar { top: 332px; top: 49px; }
  .strip--navy .agent-card { top: 102px; height: 133px; }
  .strip--white .agent-card { top: 103px; }
</style>
</head>
<body>
<main class="flyer">

  <section class="strip strip--red">
    <div class="agent-photo" role="img" aria-label="Portrait photo of sales consultant Marisska Thornbury"></div>
    <div class="pitch">
      <p class="pitch__line pitch__ask">"Are you considering selling?</p>
      <p class="pitch__line pitch__call">Call<span class="pitch__name">Marisska</span>today for a</p>
      <p class="pitch__line pitch__offer">complimentary market appraisal".</p>
    </div>
    <div class="brand-bar">KLV Realty</div>
    <div class="agent-card">
      <span class="agent-card__mark"></span>
      <p class="agent-card__name">Marisska Thornbury</p>
      <p class="agent-card__role">Sales Consultant</p>
      <p class="agent-card__phone">0400 518 294</p>
    </div>
  </section>

  <section class="strip strip--navy">
    <div class="agent-photo" role="img" aria-label="Portrait photo of sales consultant Marisska Thornbury"></div>
    <div class="pitch">
      <p class="pitch__line pitch__ask">"Are you considering selling?</p>
      <p class="pitch__line pitch__call">Call<span class="pitch__name">Marisska</span>today for a</p>
      <p class="pitch__line pitch__offer">complimentary market appraisal".</p>
    </div>
    <div class="brand-bar">KLV Realty</div>
    <div class="agent-card">
      <span class="agent-card__mark"></span>
      <p class="agent-card__name">Marisska Thornbury</p>
      <p class="agent-card__role">Sales Consultant</p>
      <p class="agent-card__phone">0400 518 294</p>
    </div>
  </section>

  <section class="strip strip--white">
    <div class="agent-photo" role="img" aria-label="Portrait photo of sales consultant Marisska Thornbury"></div>
    <div class="pitch">
      <p class="pitch__line pitch__ask">"Are you considering selling?</p>
      <p class="pitch__line pitch__call">Call<span class="pitch__name">Marisska</span>today for a</p>
      <p class="pitch__line pitch__offer">complimentary market appraisal".</p>
    </div>
    <div class="brand-bar">KLV Realty</div>
    <div class="agent-card">
      <span class="agent-card__mark"></span>
      <p class="agent-card__name">Marisska Thornbury</p>
      <p class="agent-card__role">Sales Consultant</p>
      <p class="agent-card__phone">0400 518 294</p>
    </div>
  </section>

</main>
</body>
</html>
```